Brantley Advisory Group provides support for renewable energy projects to utilities and suppliers

I need a professional looking business card that is both simple and elegant and unique. My clients are mostly large organizations not individuals. I am a consultant with my own company that is small but would like to give clients the impression I am larger. Smart grid, fiber optics, software, field hardware, distribution automation, substation automation, operations, energy storage/batteries, microgrids, customer service, strategy/roadmaps, conservation, Automated Metering Infrastruture (AMI or smart meters) are all areas of focus.

Target Market(s)

Utilities, suppliers, governmental agencies involved in energy. All types of energy especially natural gas and electrical. Especially renewable energy or green projects.

Contact Information for Business Card

Name - Mark Brantley Cell Phone - 425.318.2746 Email - mbrantley@brantleyag-example.com
Company - Brantley Advisory Group (logo) Title - Principal

Font styles to use
Serif
Sans Serif

Colors

Designer to choose colors to be used in the design.

Requirements
Must have
• Simple and professional and powerful.
• Unique/creative design.
Nice to have
• Utilize color scheme to accent logo colors. Maybe some geometric pattern on edge of card with color.
Should not have
• Busy, complicated, traditional

```html
<!DOCTYPE html>
<html lang="en">
<head>
<meta charset="utf-8">
<title>Brantley Advisory Group — Business Card</title>
<link rel="stylesheet" href="https://fonts.googleapis.com/css2?family=Arimo:wght@400;700&display=swap">
<style>
  :root {
    --backdrop: #7b7b7b;
    --card-white: #ffffff;
    --card-black: #121212;
    --brand-blue: #1f3f9c;
    --brand-green: #6f9a4a;
    --brand-grey: #a8a8a8;
    --ink: #1a1a1a;
    --rule: #9a9a9a;
  }
  * { margin: 0; padding: 0; box-sizing: border-box; }
  html, body { width: 1200px; height: 1200px; overflow: hidden; }
  body {
    background: var(--backdrop);
    font-family: "Arimo", Arial, sans-serif;
    position: relative;
  }
  .card { position: absolute; }
  .card-front {
    left: 234px; top: 310px; width: 364px; height: 594px;
    background: var(--card-white);
  }
  .card-back {
    left: 627px; top: 310px; width: 370px; height: 595px;
    background: var(--card-black);
  }
  .brand-lockup {
    position: absolute; left: 0; right: 0; top: 118px;
    display: flex; align-items: center; justify-content: center; gap: 14px;
  }
  .brand-square {
    width: 46px; height: 46px; border: 4px solid var(--brand-green); border-radius: 4px;
    flex: none;
  }
  .brand-name {
    font-weight: 700; font-size: 27px; line-height: 1.15; color: var(--brand-blue);
    width: 200px;
  }
  .contact-block {
    position: absolute; left: 0; right: 0; top: 378px; text-align: center;
  }
  .person-name {
    font-weight: 700; font-size: 27px; color: var(--brand-blue); letter-spacing: 0.2px;
  }
  .person-title { font-size: 18px; color: var(--ink); margin-top: 1px; }
  .icon-row {
    display: flex; align-items: center; justify-content: center; gap: 6px;
    margin-top: 14px;
  }
  .icon-rule { width: 50px; height: 1px; background: var(--rule); margin: 0 4px; }
  .icon-tile { width: 24px; height: 24px; border-radius: 2px; display: block; }
  .contact-lines {
    margin-top: 12px; font-size: 17px; line-height: 22px; color: var(--ink);
    list-style: none;
  }
  .back-mark {
    position: absolute; left: 0; right: 0; top: 210px;
    display: flex; flex-direction: column; align-items: center; gap: 22px;
  }
  .back-square {
    width: 110px; height: 110px; border: 8px solid var(--brand-grey); border-radius: 10px;
  }
  .back-name { font-size: 24px; font-weight: 700; color: var(--brand-grey); }
  .back-web {
    position: absolute; left: 0; right: 0; top: 528px; text-align: center;
    font-size: 17px; color: #ffffff;
  }
</style>
</head>
<body>
  <section class="card card-front">
    <div class="brand-lockup">
      <span class="brand-square"></span>
      <span class="brand-name">Brantley Advisory Group</span>
    </div>
    <div class="contact-block">
      <p class="person-name">MARK BRANTLEY</p>
      <p class="person-title">Principal</p>
      <div class="icon-row">
        <span class="icon-rule"></span>
        <svg class="icon-tile" viewBox="0 0 24 24" aria-label="Phone">
          <rect width="24" height="24" rx="2" fill="var(--brand-blue)"/>
          <path d="M5 10c0-3 14-3 14 0v1.5h-4V10H9v1.5H5z M8 12h8l2 6H6z" fill="#fff"/>
        </svg>
        <svg class="icon-tile" viewBox="0 0 24 24" aria-label="Email">
          <rect width="24" height="24" rx="2" fill="var(--brand-grey)"/>
          <rect x="5" y="7" width="14" height="10" fill="none" stroke="#fff" stroke-width="1.4"/>
          <path d="M5 7l7 6 7-6" fill="none" stroke="#fff" stroke-width="1.4"/>
        </svg>
        <svg class="icon-tile" viewBox="0 0 24 24" aria-label="Website">
          <rect width="24" height="24" rx="2" fill="var(--brand-green)"/>
          <circle cx="12" cy="12" r="7" fill="#fff"/>
          <ellipse cx="12" cy="12" rx="3" ry="7" fill="none" stroke="var(--brand-green)" stroke-width="1.2"/>
          <path d="M5 12h14" stroke="var(--brand-green)" stroke-width="1.2"/>
        </svg>
        <span class="icon-rule"></span>
      </div>
      <ul class="contact-lines">
        <li>425.318.2746</li>
        <li>mbrantley@brantleyag-example.com</li>
        <li>www.brantleyag-example.com</li>
      </ul>
    </div>
  </section>

  <section class="card card-back">
    <div class="back-mark">
      <span class="back-square"></span>
      <span class="back-name">Brantley Advisory Group</span>
    </div>
    <p class="back-web">www.brantleyag-example.com</p>
  </section>
</body>
</html>
```